New Web Design Project for New Criminal Defense Firm

I need a attention getting, professional but edgy website. I have been working as a prosecutor for the last 10 years and am opening my own law firm. I need to demonstrate trust, professionalism and grit. I have attached my logo. I will be representing criminals and am board certified in criminal law (which is a big deal in Texas). Honesty and integrity are key. Currently, I am using a website by website builder and I think it could be much more refined, it is lame. https://parveck-holtbylaw.com/
Here is a link for you to check it out.

Target Market(s)

Those charged with crimes ranging from DWIs to Murder

Industry/Entity Type

Law Firm

Coding

Coded - Design and coding required

Number of Pages Required

3 page

Font styles to use
Serif

Colors
3176b5
fbee3d

Requirements
Must have
• Contact us, about us

```html
<!DOCTYPE html>
<html lang="en">
<head>
<meta charset="utf-8">
<title>Parveck-Holtby Law</title>
<link href="https://fonts.googleapis.com/css2?family=Tinos:wght@400;700&family=Questrial&display=swap" rel="stylesheet">
<style>
:root{
  --blue:#2f75b5;
  --gold:#d9b77f;
  --ink:#1b1b1b;
  --grey-text:#555;
  --dark:#3b3a3d;
  --light:#f2f2f2;
  --white:#fff;
}
*{box-sizing:border-box;margin:0;padding:0}
html,body{width:1200px;height:2481px;overflow:hidden}
body{position:relative;background:var(--white);font-family:'Questrial',sans-serif;color:var(--ink)}
.abs{position:absolute}
.serif{font-family:'Tinos',serif;font-weight:400}

/* header */
.site-header{left:0;top:0;width:1200px;height:96px;background:var(--white)}
.brand{left:85px;top:28px;display:flex;align-items:center;gap:10px}
.brand-mark{width:34px;height:34px;border:2px solid var(--gold)}
.brand-name{font-family:'Tinos',serif;color:var(--gold);font-size:20px;line-height:20px;letter-spacing:1px}
.nav{top:40px;font-size:13px;color:var(--ink)}
.nav a{position:absolute;white-space:nowrap;color:inherit;text-decoration:none}
.nav .active{color:var(--gold)}
.nav-call{left:800px;top:39px;font-size:14.5px;color:var(--gold);white-space:nowrap}
.nav-call span{color:var(--blue)}
.social{display:flex;gap:7px}
.social i{display:block;width:34px;height:34px;border-radius:50%;background:var(--blue)}
.social i.gold{background:var(--gold)}
.header-social{left:999px;top:31px}

/* hero */
.hero{left:0;top:96px;width:1200px;height:548px;background:linear-gradient(135deg,#2a2a2c 0%,#5a5048 45%,#7c6a55 60%,#2c3b55 100%)}
.hero-shade{left:0;top:96px;width:1200px;height:548px;background:rgba(20,20,25,.45)}
.hero-brand{left:0;width:1200px;top:255px;text-align:center;color:var(--white);font-family:'Tinos',serif;font-size:38px;letter-spacing:2px}
.hero-title{left:0;width:1200px;top:356px;text-align:center;color:var(--white);font-size:40px;line-height:48px}
.btn-outline{border:2px solid var(--gold);color:var(--gold);border-radius:22px;font-size:13px;display:flex;align-items:center;justify-content:center;letter-spacing:.3px}
.hero-btn{left:511px;top:481px;width:178px;height:40px}

/* about */
.about{left:0;top:644px;width:640px;height:499px;background:var(--blue)}
.about-portrait{left:640px;top:644px;width:560px;height:499px;background:linear-gradient(160deg,#c9c6c2 0%,#a88a6a 40%,#e1c8b0 60%,#9c3a34 100%)}
.eyebrow{font-size:16px}
.about .eyebrow{left:85px;top:78px;color:var(--white)}
.section-title{font-size:29px;line-height:35px}
.about .section-title{left:85px;top:116px;width:480px;color:var(--white)}
.body-copy{font-size:13.5px;line-height:19.5px}
.about .body-copy{left:85px;top:282px;width:480px;color:var(--white)}
.btn-solid{background:var(--gold);color:var(--white);border-radius:22px;font-size:13px;display:flex;align-items:center;justify-content:center}
.about .btn-solid{left:85px;top:376px;width:145px;height:40px}

/* what we do */
.exp-strip{left:85px;top:1225px;width:47px;height:361px;background:var(--gold)}
.exp-label{left:85px;top:1225px;width:47px;height:361px;display:flex;align-items:center;justify-content:center}
.exp-label span{transform:rotate(-90deg);white-space:nowrap;color:var(--white);font-size:19px;letter-spacing:1px}
.gavel-photo{left:132px;top:1225px;width:242px;height:361px;background:linear-gradient(170deg,#5a4a3c 0%,#8a6e55 40%,#4a2c1c 70%,#b59e86 100%)}
.gavel-notch{left:326px;top:1410px;width:48px;height:176px;background:var(--white)}
.mark-card{left:342px;top:1426px;width:218px;height:208px;background:var(--blue);display:flex;align-items:center;justify-content:center}
.mark-card span{font-family:'Tinos',serif;color:var(--gold);font-size:24px}
.services .eyebrow{left:640px;top:1250px;color:var(--gold)}
.services .section-title{left:640px;top:1288px;width:460px;color:#1f2a3a}
.services .body-copy{left:640px;top:1455px;width:450px;color:var(--grey-text)}
.services .btn-outline{left:640px;top:1567px;width:145px;height:40px}

/* cta */
.cta{left:0;top:1715px;width:1200px;height:161px;background:var(--blue)}
.cta-title{left:206px;top:48px;color:var(--white);font-size:33px}
.cta-sub{left:206px;top:90px;color:var(--white);font-size:18px}
.cta-btn{left:786px;top:61px;width:209px;height:40px;border:2px solid var(--gold);color:var(--gold);font-size:13px;display:flex;align-items:center;justify-content:center}

/* contact */
.contact-info{left:0;top:1876px;width:600px;height:524px;background:linear-gradient(120deg,#2e2d30 0%,#4a4749 50%,#333135 100%)}
.contact-info .firm{left:204px;top:62px;color:var(--gold);font-size:20px}
.contact-info .phone{left:205px;top:104px;color:var(--blue);font-size:25px}
.contact-info .email{left:205px;top:142px;color:#ddd;font-size:13.5px}
.contact-info .email b{color:var(--gold);font-weight:400}
.info-label{color:var(--gold);font-size:14px;font-weight:700;font-family:'Questrial',sans-serif}
.info-text{color:#ddd;font-size:13.5px;line-height:19.5px}
.contact-social{left:205px;top:327px}
.badge{left:205px;top:399px;width:180px;height:72px;border:2px solid #ddd}
.booking{left:600px;top:1876px;width:600px;height:524px;background:var(--light)}
.booking .form-title{left:71px;top:62px;color:var(--blue);font-size:20px}
.field{left:72px;width:323px;height:34px;background:var(--white);border:1px solid #e6e6e6;font-size:11px;color:#999;padding:10px 15px}
.submit{left:71px;top:422px;width:129px;height:40px}

/* footer */
.footer-note{left:0;top:2429px;width:1200px;text-align:center;font-size:13px;color:#333}
.footer-note span{color:var(--gold)}
.to-top{left:1114px;top:2425px}
</style>
</head>
<body>

<header class="site-header abs">
  <div class="brand abs"><i class="brand-mark"></i><span class="brand-name">PARVECK-HOLTBY</span></div>
  <nav class="nav abs" style="left:0;width:1200px">
    <a class="active" style="left:505px">Home</a>
    <a style="left:582px">About Us</a>
    <a style="left:680px">Contact Us</a>
  </nav>
  <div class="nav-call abs">Call: <span>(361)555-0192</span></div>
  <div class="social header-social abs" aria-label="Social links"><i></i><i class="gold"></i><i></i></div>
</header>

<section class="hero abs" role="img" aria-label="Photo of a lawyer shaking hands with a client across a desk"></section>
<div class="hero-shade abs"></div>
<div class="hero-brand abs">Parveck-Holtby</div>
<h1 class="hero-title abs serif">Maren and her team are ready to passionately<br>defend your rights.</h1>
<div class="hero-btn btn-outline abs">Book An Appointment</div>

<section class="about abs">
  <div class="eyebrow abs">About Us</div>
  <h2 class="section-title abs serif">Maren Parveck-Holtby is Board Certified by the state specialization board in Criminal Law, making her a specialist in her field.</h2>
  <p class="body-copy abs">Maren Parveck-Holtby, former First Assistant for Calder County District Attorney, has 10 years of experience as an effective criminal trial lawyer and high-level prosecutor. of legal expertise ...</p>
  <div class="btn-solid abs">Discover More</div>
</section>
<div class="about-portrait abs" role="img" aria-label="Portrait photo of the attorney"></div>

<section class="services">
  <div class="exp-strip abs"></div>
  <div class="gavel-photo abs" role="img" aria-label="Photo of a wooden gavel and scales of justice"></div>
  <div class="gavel-notch abs"></div>
  <div class="exp-label abs"><span>10 Years of Experience</span></div>
  <div class="mark-card abs"><span>Parveck-Holtby</span></div>
  <div class="eyebrow abs">What We Do</div>
  <h2 class="section-title abs serif">We offer representation for all criminal allegations from DWI to aggravated assault and all offenses in between.</h2>
  <p class="body-copy abs">The criminal justice system can be confusing and embarrassing. The outcome of your case can be possibly be detrimental to your life and to those around you. Take comfort knowing that the defense team at Parveck-Holtby Law are on your case.</p>
  <div class="btn-outline abs">Contact Us</div>
</section>

<section class="cta abs">
  <div class="cta-title abs serif">Are you having any problems</div>
  <div class="cta-sub abs">But can't consult to anyone?</div>
  <div class="cta-btn abs">Contact Us Today!</div>
</section>

<section class="contact-info abs" role="img" aria-label="Dark photo of a Lady Justice statue behind contact details">
  <div class="firm abs">Parveck-Holtby Law</div>
  <div class="phone abs">Call. (361)555-0192</div>
  <div class="email abs"><b>e.</b> Maren@Parveck-HoltbyLaw.com</div>
  <div class="abs" style="left:205px;top:185px">
    <div class="info-label">Address:</div>
    <div class="info-text">PO Box 2205 Bayview, TX 78300</div>
  </div>
  <div class="abs" style="left:205px;top:243px">
    <div class="info-label">Office Hours:</div>
    <div class="info-text">Monday to Saturday: 9:00 - 18:00<br>Sunday: Closed</div>
  </div>
  <div class="social contact-social abs"><i></i><i class="gold"></i><i></i></div>
  <div class="badge abs" aria-label="Board certification badge"></div>
</section>

<section class="booking abs">
  <div class="form-title abs">Book Free Consultation</div>
  <div class="field abs" style="top:111px">Your Name</div>
  <div class="field abs" style="top:161px">Email</div>
  <div class="field abs" style="top:211px">Phone</div>
  <div class="field abs" style="top:261px;height:136px">Message ...</div>
  <div class="submit btn-solid abs">Submit</div>
</section>

<footer>
  <div class="footer-note abs">© 2020 <span>Parveck-Holtby Law</span> All Right Reserved</div>
  <svg class="to-top abs" width="18" height="22" viewBox="0 0 18 22" aria-label="Back to top"><path d="M9 1 L17 21 L9 15 L1 21 Z" fill="none" stroke="#2f75b5" stroke-width="1.6" stroke-linejoin="round"/></svg>
</footer>

</body>
</html>
```